Quillrests.com website overhaul

We want to upgrade our Wix website into a professional looking page for our growing business. The content that is online now needs to be used but the site should have a new look and feel from top to bottom. QuillRests is a company in the hospital and nursing home space. We would like to see the website use our color scheme but other than that we are open to any and all ideas. www.quillrests.com

```html
<!DOCTYPE html>
<html lang="en">
<head>
<meta charset="utf-8">
<title>QuillRests — Air Filtration System</title>
<link href="https://fonts.googleapis.com/css2?family=Lexend:wght@400;500;600;700&family=Inter:wght@400;500;600&display=swap" rel="stylesheet">
<style>
:root{
  --topbar:#2b0f4e;
  --indigo:#4652a3;
  --indigo-dark:#3a4590;
  --ink:#111;
  --body:#333;
  --muted:#555;
  --soft:#f4f4fb;
  --band:#2e1157;
  --footer:#1d1d22;
  --white:#fff;
}
*{box-sizing:border-box;margin:0;padding:0}
html,body{width:1200px;height:3990px;overflow:hidden}
body{position:relative;font-family:"Inter",sans-serif;color:var(--body);background:var(--white)}
h1,h2,h3,.brand,.btn{font-family:"Lexend",sans-serif}
.abs{position:absolute}

/* top bar */
.topbar{position:absolute;top:0;left:0;width:1200px;height:47px;background:var(--topbar);color:#fff;font-size:16px}
.topbar .social{position:absolute;left:96px;top:13px;display:flex;gap:14px}
.topbar .social span{width:20px;height:20px;border-radius:4px;background:#fff;opacity:.9}
.topbar .contacts{position:absolute;right:96px;top:12px;display:flex;gap:20px;align-items:center}
.topbar .contacts span{display:flex;align-items:center;gap:7px}

/* hero */
.hero{position:absolute;top:47px;left:0;width:1200px;height:595px;background:linear-gradient(180deg,#5a6478 0%,#59627a 55%,#6d6258 100%)}
.hero-art{position:absolute;inset:0}
.nav{position:absolute;top:0;left:0;width:100%;height:90px}
.brand{display:flex;align-items:center;gap:12px;color:#fff;font-weight:500;font-size:38px}
.brand .mark{width:34px;height:34px;background:#fff;border-radius:4px}
.brand .rule{width:2px;height:58px;background:#fff}
.nav .brand{position:absolute;left:99px;top:15px}
.nav ul{position:absolute;right:96px;top:34px;display:flex;gap:48px;list-style:none;color:#fff;font-family:"Lexend",sans-serif;font-weight:600;font-size:17px}
.hero h1{position:absolute;top:210px;width:100%;text-align:center;color:#fff;font-size:60px;font-weight:600;line-height:68px}
.btn{display:inline-flex;align-items:center;gap:8px;font-weight:600;border-radius:30px}
.hero .btn{position:absolute;left:516px;top:372px;width:168px;height:47px;justify-content:center;border:2px solid #fff;color:#fff;font-size:17px}
.hero .arrow{position:absolute;top:267px}

/* intro */
.intro-media{position:absolute;left:96px;top:755px;width:481px;height:366px;background:linear-gradient(180deg,#5c6f86 0%,#8ea2b8 15%,#b8c7d6 60%,#c98f72 95%)}
.play{position:absolute;left:195px;top:138px;width:90px;height:90px;border:5px solid #fff;border-radius:50%}
.intro-text{position:absolute;left:615px;top:742px;width:490px}
.intro-text h2{font-size:42px;font-weight:600;line-height:48px;color:var(--ink)}
.intro-text p{margin-top:20px;font-size:15px;line-height:28.5px;color:var(--body)}

/* how it works */
.section-title{position:absolute;width:100%;text-align:center;font-family:"Lexend",sans-serif;font-weight:600;color:var(--ink);font-size:42px}
.pill{position:absolute;height:110px;border:2px solid #333;border-radius:55px;font-size:15px;line-height:21px;color:#222;display:flex;align-items:center}
.pill.left{border-right:none;border-radius:55px 0 0 55px;padding:0 30px 0 33px}
.pill.right{border-left:none;border-radius:0 55px 55px 0;padding:0 26px 0 36px}
.num{position:absolute;width:100px;height:100px;border-radius:50%;background:#fff;border:7px solid var(--indigo);box-shadow:0 0 0 4px #fff,0 0 0 6px #ccc;display:flex;align-items:center;justify-content:center;font-family:"Lexend",sans-serif;font-weight:600;font-size:42px;color:var(--indigo)}
.hub{position:absolute;left:483px;top:1494px;width:232px;height:232px;border-radius:50%;background:radial-gradient(circle at 50% 40%,#fff 0%,#eee 60%,#cfcfd6 100%);display:flex;align-items:center;justify-content:center}
.hub .brand{font-size:24px;color:var(--indigo);gap:9px}
.hub .brand .mark{width:22px;height:22px;background:var(--indigo)}
.hub .brand .rule{height:40px;background:var(--indigo)}

/* features */
.features{position:absolute;top:1958px;left:0;width:1200px;height:805px;background:var(--soft)}
.features .sub{position:absolute;top:145px;width:100%;text-align:center;font-size:17px;color:#222}
.card{position:absolute;top:214px;width:316px;height:485px;background:#fff;border-radius:6px;overflow:hidden;box-shadow:0 2px 8px rgba(0,0,0,.05)}
.card .pic{height:206px}
.card .body{padding:24px 19px}
.card h3{font-size:22px;font-weight:600;line-height:26px;color:var(--ink)}
.card p{margin-top:14px;font-size:15px;line-height:24px;color:var(--body)}
.card .more{margin-top:6px;color:var(--indigo);font-family:"Lexend",sans-serif;font-weight:600;font-size:16px}
.card.active{background:var(--indigo)}
.card.active h3,.card.active p{color:#fff}

/* contact */
.field{position:absolute;border:1px solid #555;border-radius:2px;font-size:15px;color:#333;padding:18px 14px}
.submit{position:absolute;left:525px;top:3255px;width:150px;height:48px;justify-content:center;background:var(--indigo);color:#fff;font-size:17px}

/* band */
.band{position:absolute;top:3390px;left:0;width:1200px;height:256px;background:linear-gradient(90deg,#2c0f4f,#341463 60%,#2c0f4f)}
.band h2{position:absolute;left:97px;top:70px;color:#fff;font-size:42px;font-weight:600;line-height:48px}
.band p{position:absolute;left:527px;top:78px;color:#fff;font-size:15px}
.band .btn{position:absolute;left:527px;top:118px;height:48px;padding:0 24px;border:2px solid #fff;color:#fff;font-size:17px}

/* footer */
.footer{position:absolute;top:3646px;left:0;width:1200px;height:344px;background:var(--footer);color:#ddd}
.footer .brand{position:absolute;left:99px;top:90px;font-size:36px}
.footer .icons{position:absolute;left:148px;top:184px;display:flex;gap:14px}
.footer .icons span{width:32px;height:32px;border-radius:50%;background:#fff}
.footer h4{font-family:"Lexend",sans-serif;font-weight:600;font-size:20px;color:#fff;position:absolute;top:82px}
.footer ul{position:absolute;top:128px;list-style:none;font-size:15px;line-height:36px;color:#ddd}
.footer .news{position:absolute;left:846px;top:127px;width:256px;height:46px;background:#fff;border:1px solid #ccc;font-size:15px;color:#666;padding:13px 11px}
.footer .sub-btn{position:absolute;left:846px;top:186px;height:50px;padding:0 20px;background:var(--indigo);color:#fff;font-size:18px}
.footer .legal{position:absolute;top:310px;font-size:13px;color:#888}
</style>
</head>
<body>

<header class="topbar">
  <div class="social"><span></span><span></span><span></span><span></span></div>
  <div class="contacts">
    <span><svg width="16" height="12" viewBox="0 0 16 12"><rect x="0.5" y="0.5" width="15" height="11" fill="none" stroke="#8f9cf0"/><path d="M1 1l7 6 7-6" fill="none" stroke="#8f9cf0"/></svg>hello@quillrests.com</span>
    <span><svg width="14" height="14" viewBox="0 0 24 24"><path d="M6.6 10.8a15 15 0 006.6 6.6l2.2-2.2a1 1 0 011-.25 11 11 0 003.6.6 1 1 0 011 1V20a1 1 0 01-1 1A17 17 0 013 4a1 1 0 011-1h3.5a1 1 0 011 1 11 11 0 00.6 3.6 1 1 0 01-.25 1z" fill="#8f9cf0"/></svg>555-014-2276</span>
  </div>
</header>

<section class="hero">
  <div class="hero-art" role="img" aria-label="Illustration of a hospital room with a filtration panel and air filter panels, dimmed behind the headline"></div>
  <nav class="nav">
    <div class="brand"><span class="mark"></span><span class="rule"></span>QuillRests</div>
    <ul><li>Home</li><li>How it Works</li><li>Resources</li><li>Contact</li></ul>
  </nav>
  <svg class="arrow" style="left:98px" width="36" height="70" viewBox="0 0 36 70"><path d="M34 2L2 35l32 33" fill="none" stroke="#fff" stroke-width="2.5"/></svg>
  <svg class="arrow" style="left:1066px" width="36" height="70" viewBox="0 0 36 70"><path d="M2 2l32 33L2 68" fill="none" stroke="#fff" stroke-width="2.5"/></svg>
  <h1>QuillRest is an<br>air Filtration System</h1>
  <span class="btn">Contact Us <svg width="14" height="12" viewBox="0 0 14 12"><path d="M0 6h12M7 1l5 5-5 5" fill="none" stroke="#fff" stroke-width="1.8"/></svg></span>
</section>

<section>
  <div class="intro-media" role="img" aria-label="Video still of a patient room with bed, cabinet and filtration unit">
    <div class="play"><svg width="80" height="80" viewBox="0 0 80 80"><path d="M30 22l28 18-28 18z" fill="#fff"/></svg></div>
  </div>
  <div class="intro-text">
    <h2>Enhanced Protection Against Airborne Infectious Particles</h2>
    <p>The QuillRest is an air filtration system that reduces the exposure to airborne infectious particles for healthcare workers, patients, and visitors by utilizing a source-focused technology that captures airborne infectious particles at the source. The QuillRest utilizes a patent-pending headboard design that pulls air from the head area of the patient through a HEPA filtration system and exhausts filtered air back into the room.</p>
  </div>
</section>

<section>
  <h2 class="section-title" style="top:1265px">How a QuillRest Works</h2>
  <svg class="abs" style="left:0;top:1370px" width="1200" height="490" viewBox="0 0 1200 490">
    <circle cx="599" cy="240" r="150" fill="none" stroke="#333" stroke-width="2"/>
    <circle cx="599" cy="240" r="133" fill="var(--indigo)"/>
    <g fill="#222"><circle cx="502" cy="122" r="11"/><circle cx="698" cy="122" r="11"/><circle cx="446" cy="240" r="11"/><circle cx="754" cy="240" r="11"/><circle cx="502" cy="358" r="11"/><circle cx="698" cy="358" r="11"/></g>
    <g fill="var(--indigo)">
      <path d="M440 50l45 42-18 20z"/><path d="M760 50l-45 42 18 20z"/>
      <path d="M395 215l40 25-40 25z"/><path d="M805 215l-40 25 40 25z"/>
      <path d="M440 430l45-42-18-20z"/><path d="M760 430l-45-42 18-20z"/>
    </g>
  </svg>
  <div class="hub"><div class="brand"><span class="mark"></span><span class="rule"></span>QuillRests</div></div>

  <div class="pill left" style="left:99px;top:1378px;width:300px">A resident shows possible symptoms of an illness or virus.</div>
  <div class="num" style="left:383px;top:1384px">01</div>
  <div class="pill left" style="left:99px;top:1543px;width:226px;height:140px;font-size:14.5px;padding:0 18px 0 18px">Install QuillRest System to patient bed and turn on HEPA box on to protect other residents, healthcare workers, and visitors from..</div>
  <div class="num" style="left:306px;top:1563px">02</div>
  <div class="pill left" style="left:99px;top:1735px;width:300px;padding-left:30px">The QuillRest uses negative air pressure to help with aerosol containment before contaminants have a chance to disperse.</div>
  <div class="num" style="left:383px;top:1738px">03</div>

  <div class="pill right" style="left:799px;top:1378px;width:300px">The HEPA filtration reduces the number of airborne infectious particles helping protect the air and surrounding surfaces from contamination.</div>
  <div class="num" style="left:715px;top:1384px">04</div>
  <div class="pill right" style="left:875px;top:1543px;width:224px;height:140px">The canopy allows low-velocity air currents to capture and remove airborne infectious particles without irritating the patient.</div>
  <div class="num" style="left:791px;top:1563px">05</div>
  <div class="pill right" style="left:799px;top:1735px;width:300px">A typical 20 x 15 patient room will have the air completely turned over and cleaned approximately every 9 minutes.</div>
  <div class="num" style="left:715px;top:1738px">06</div>
</section>

<section class="features">
  <h2 class="section-title" style="top:82px">Source-Focused HEPA Filtration</h2>
  <p class="sub">Capture airborne infectious particles at the source</p>
  <article class="card" style="left:99px">
    <div class="pic" role="img" aria-label="Illustration of a nurse beside a patient resting in bed" style="background:linear-gradient(180deg,#1f97c4 0%,#2aa3cf 70%,#e8eef4 100%)"></div>
    <div class="body">
      <h3>Greater Protection than an N95 Mask*</h3>
      <p>According to the NHA Study, "Expedient Methods for Surge Airborne Isolation within Healthcare Settings during Response to a Natural or Manmade Epidemic", the expedient airborne isolation</p>
      <p class="more">Read More &rarr;</p>
    </div>
  </article>
  <article class="card active" style="left:443px">
    <div class="pic" role="img" aria-label="Illustration of filtration panel and air filters above a bed" style="background:linear-gradient(180deg,#6f7f99 0%,#8c98ad 60%,#2d4a8e 100%)"></div>
    <div class="body">
      <h3>Deploys in Minutes</h3>
      <p>The QuillRest is a complete system that can be deployed in a matter of minutes using only basic tools. The system easily disassembles for sanitation.</p>
    </div>
  </article>
  <article class="card" style="left:785px">
    <div class="pic" role="img" aria-label="Illustration of a patient room with bed, cabinet and filtration unit" style="background:linear-gradient(180deg,#c5d3e0 0%,#dde6ee 60%,#4a78b8 100%)"></div>
    <div class="body">
      <h3>9 Minutes</h3>
      <p>Turns over air in a 15 x 20 room in 9 minutes.</p>
    </div>
  </article>
</section>

<section>
  <h2 class="section-title" style="top:2838px">Get In Touch</h2>
  <div class="field" style="left:166px;top:2907px;width:433px;height:56px">Name</div>
  <div class="field" style="left:611px;top:2907px;width:434px;height:56px">Email</div>
  <div class="field" style="left:166px;top:2975px;width:433px;height:56px">Phone</div>
  <div class="field" style="left:611px;top:2975px;width:434px;height:56px;padding-left:2px">Subjecet</div>
  <div class="field" style="left:166px;top:3045px;width:879px;height:54px">Address</div>
  <div class="field" style="left:166px;top:3112px;width:879px;height:131px">Message</div>
  <span class="btn submit">Submit &rarr;</span>
</section>

<section class="band">
  <h2>QuillRests PDF<br>Quick Info Sheet</h2>
  <p>Quick download for a printable information piece on the QuillRests system.</p>
  <span class="btn">QuillRest PDF Quick Info Sheet &nbsp;&rarr;</span>
</section>

<footer class="footer">
  <div class="brand"><span class="mark"></span><span class="rule"></span>QuillRests</div>
  <div class="icons"><span></span><span></span><span></span><span></span></div>
  <h4 style="left:416px">Quick Links</h4>
  <ul style="left:416px"><li>Home</li><li>How it Works</li><li>Resources</li><li>Contact</li></ul>
  <h4 style="left:594px">Contact Info</h4>
  <ul style="left:594px"><li>&#9993;&nbsp; hello@quillrests.com</li><li>&#9742;&nbsp; 555-014-2276</li></ul>
  <h4 style="left:846px">Newsletter</h4>
  <div class="news">Enter email Address</div>
  <span class="btn sub-btn" style="display:inline-flex;align-items:center">Subscribe &rarr;</span>
  <p class="legal" style="left:99px">&copy; 2022 <b style="color:#fff;font-weight:600">Quillrests</b>. All right reserved</p>
  <p class="legal" style="right:99px">Dec 20, 2022. Layout_4</p>
</footer>

</body>
</html>
```